PEAK KENNEL - business card
A way to remember us and buy our products
Professional
PEAKKENNEL - the finest pick
Lindmarkv. 24
SE-712 46 Eskilstuna
SWEDEN
info@peakkennel-demo.se
www.peakkennel-demo.se
I would like the business cards and other material to match.
It is about dogs and our show trolley.
I need something to hand out as I meet people at dog shows or otherwise.
your ideas are welcome to figure out what the backside should be.
drawing of product_logo related
LOGO in whole, van be split into two
4 berth
LOGO PDF
drawing pdf
Product today. Steel 2 berth

```html
<!DOCTYPE html>
<html lang="en">
<head>
<meta charset="utf-8">
<title>PEAK KENNEL – Business Card</title>
<link rel="stylesheet" href="https://fonts.googleapis.com/css2?family=Fjalla+One&family=Open+Sans:wght@400;700&display=swap">
<style>
  :root {
    --brand-blue: #1f5da8;
    --brand-orange: #f0901e;
    --ink: #333a44;
    --muted: #6b7280;
    --rule: #c9ced6;
    --paper: #ffffff;
    --backdrop: #e9ebef;
    --card-edge: #d5d9df;
  }
  * { margin: 0; padding: 0; box-sizing: border-box; }
  html, body {
    width: 1200px;
    height: 646px;
    overflow: hidden;
    background: var(--backdrop);
  }
  .card-sheet {
    position: relative;
    width: 1200px;
    height: 646px;
    font-family: "Open Sans", Arial, sans-serif;
    color: var(--ink);
  }
  .card {
    position: absolute;
    top: 164px;
    width: 555px;
    height: 318px;
    background: var(--paper);
    border: 1px solid var(--card-edge);
    overflow: hidden;
  }
  .card-back { left: 30px; }
  .card-front { left: 615px; }

  /* Back side */
  .back-brand {
    position: absolute;
    left: 0;
    top: 0;
    width: 100%;
    height: 100%;
    display: flex;
    flex-direction: column;
    align-items: center;
    justify-content: center;
  }
  .back-mark {
    width: 70px;
    height: 70px;
    background: var(--brand-blue);
  }
  .back-name {
    margin-top: 12px;
    font-family: "Fjalla One", "Arial Narrow", sans-serif;
    font-size: 28px;
    line-height: 1;
    letter-spacing: 0.5px;
    color: var(--brand-orange);
  }
  .back-website {
    margin-top: 10px;
    font-size: 10px;
    color: var(--ink);
  }

  /* Front side */
  .brand {
    position: absolute;
    left: 110px;
    top: 52px;
    display: flex;
    align-items: center;
    gap: 12px;
  }
  .brand-mark {
    width: 42px;
    height: 42px;
    flex: none;
    background: var(--brand-blue);
  }
  .brand-text { display: flex; flex-direction: column; }
  .brand-name {
    font-family: "Fjalla One", "Arial Narrow", sans-serif;
    font-size: 44px;
    line-height: 1;
    letter-spacing: 0.5px;
    color: var(--brand-orange);
  }
  .brand-tagline {
    margin-top: 3px;
    font-size: 10px;
    color: var(--muted);
  }
  .contact-person {
    position: absolute;
    left: 60px;
    top: 146px;
    width: 150px;
    text-align: right;
  }
  .person-name {
    font-size: 16px;
    font-weight: 700;
    color: var(--brand-blue);
    margin-bottom: 4px;
  }
  .address-line {
    font-size: 11px;
    line-height: 1.45;
  }
  .divider {
    position: absolute;
    left: 224px;
    top: 146px;
    width: 1px;
    height: 80px;
    background: var(--rule);
  }
  .contact-list {
    position: absolute;
    left: 238px;
    top: 152px;
    list-style: none;
  }
  .contact-item {
    display: flex;
    align-items: center;
    gap: 8px;
    font-size: 11px;
    line-height: 1;
    margin-bottom: 10px;
  }
  .contact-icon {
    width: 14px;
    height: 14px;
    flex: none;
  }
  .footer-waves {
    position: absolute;
    left: 0;
    bottom: 0;
    width: 555px;
    height: 100px;
  }
</style>
</head>
<body>
  <main class="card-sheet">
    <section class="card card-back">
      <div class="back-brand">
        <div class="back-mark"></div>
        <span class="back-name">PEAKKENNEL</span>
        <span class="back-website">www.peakkennel-demo.se</span>
      </div>
    </section>

    <section class="card card-front">
      <header class="brand">
        <div class="brand-mark"></div>
        <div class="brand-text">
          <span class="brand-name">PEAKKENNEL</span>
          <span class="brand-tagline">A way to remember us and buy our products</span>
        </div>
      </header>

      <div class="contact-person">
        <p class="person-name">Your Name</p>
        <p class="address-line">Lindmarkv. 24</p>
        <p class="address-line">SE-712 46 Eskilstuna</p>
        <p class="address-line">SWEDEN</p>
      </div>

      <div class="divider"></div>

      <ul class="contact-list">
        <li class="contact-item">
          <svg class="contact-icon" viewBox="0 0 26 26" aria-hidden="true">
            <rect x="6" y="2" width="14" height="22" rx="3" fill="var(--brand-blue)"/>
            <rect x="8.5" y="5" width="9" height="13" fill="#fff"/>
            <circle cx="13" cy="21" r="1.4" fill="#fff"/>
          </svg>
          <span>+46 70 555 0142</span>
        </li>
        <li class="contact-item">
          <svg class="contact-icon" viewBox="0 0 26 26" aria-hidden="true">
            <circle cx="13" cy="13" r="12" fill="var(--brand-blue)"/>
            <rect x="6.5" y="8.5" width="13" height="9" fill="#fff"/>
            <path d="M6.5 8.5 L13 14 L19.5 8.5" fill="none" stroke="var(--brand-blue)" stroke-width="1.4"/>
          </svg>
          <span>info@peakkennel-demo.se</span>
        </li>
        <li class="contact-item">
          <svg class="contact-icon" viewBox="0 0 26 26" aria-hidden="true">
            <circle cx="13" cy="13" r="11" fill="none" stroke="var(--brand-blue)" stroke-width="2"/>
            <ellipse cx="13" cy="13" rx="5" ry="11" fill="none" stroke="var(--brand-blue)" stroke-width="1.6"/>
            <line x1="2" y1="13" x2="24" y2="13" stroke="var(--brand-blue)" stroke-width="1.6"/>
          </svg>
          <span>www.peakkennel-demo.se</span>
        </li>
      </ul>

      <svg class="footer-waves" viewBox="0 0 555 100" preserveAspectRatio="none" aria-hidden="true">
        <path d="M0 76 C 160 76, 370 66, 555 18" fill="none" stroke="var(--brand-orange)" stroke-width="3"/>
        <path d="M0 88 C 175 86, 380 76, 555 32 L555 100 L0 100 Z" fill="var(--brand-blue)"/>
      </svg>
    </section>
  </main>
</body>
</html>
```